Healthy lifestyle Influencer business card

I need your creativity to have a business card that I can leave in all the restaurants, hotels and spas I visit to inform them that I am an influencer specializing in the wellness sector and that I will write a review about them. You can use my instagram photos Velusport72 or on my website www.piattileggerinuovi.it. I would like my business card to impress with its creativity! thank you very much!

Contact Information for Business Card

siteweb, instagram, phone number

Font styles to use
Decorative
Script

Colors
0094D4
00A9DD
6FCCEA
C7EBF8
E9F6FB
59FF00
82FF00
B8FF75
E3FFCB
F4FFEA
FFC000
F8CF3A
FAE287
FDF2CF
FEFAEE
F0912C
F2A743
F7CA91
FBE8D2
FDF5EE
EE7325
F08F49
F5BC92
FAE3D3
FDF4ED
EB3D1F
EC4F4E
F09395
F8D3D4
FCEDEE
E54698
E96AAD
F1A4CE
F9D9EA
FCEFF6

Requirements
Nice to have
• creativity

```html
<!DOCTYPE html>
<html lang="it">
<head>
<meta charset="utf-8">
<title>Velusport Chef – Biglietto da visita</title>
<link rel="stylesheet" href="https://fonts.googleapis.com/css2?family=Montserrat:wght@500;700&family=Open+Sans:wght@400&display=swap">
<style>
  :root {
    --canvas: #2b2b2b;
    --peach: #f3dcc4;
    --peach-deep: #efd2b4;
    --white: #ffffff;
    --ink: #3d3d3d;
    --ink-soft: #555555;
    --photo-warm: #d9b25a;
    --photo-light: #efe3cf;
    --accent-pink: #e54698;
  }
  * { box-sizing: border-box; margin: 0; padding: 0; }
  html, body { width: 1200px; height: 1015px; overflow: hidden; background: var(--canvas); }
  .canvas { position: relative; width: 1200px; height: 1015px; }

  .card {
    position: absolute; left: 250px; width: 700px; height: 400px;
    overflow: hidden; box-shadow: 0 10px 30px rgba(0,0,0,.45);
  }
  .card--back { top: 80px; background: var(--peach); }
  .card--front { top: 535px; background: var(--white); }

  .brand-name {
    font-family: "Montserrat", sans-serif; font-weight: 500;
    letter-spacing: .5px; white-space: nowrap;
  }
  .card--back .brand {
    position: absolute; inset: 0; display: flex; align-items: center; justify-content: center; gap: 14px;
  }
  .card--back .brand-name { color: var(--white); font-size: 46px; }
  .card--back .brand-dot { width: 16px; height: 16px; border-radius: 50%; background: var(--white); }

  .photo { position: absolute; inset: 0; width: 700px; height: 400px; }

  .card--front .brand {
    position: absolute; left: 70px; top: 78px; display: flex; align-items: center; gap: 10px;
  }
  .card--front .brand-dot { width: 12px; height: 12px; border-radius: 50%; background: var(--peach-deep); }
  .card--front .brand-name { color: var(--ink-soft); font-size: 30px; }

  .person { position: absolute; left: 70px; top: 196px; }
  .person-name { font-family: "Montserrat", sans-serif; font-weight: 700; font-size: 26px; color: var(--ink); }
  .person-role { font-family: "Open Sans", sans-serif; font-size: 17px; color: var(--ink); margin-top: 2px; }

  .contacts { position: absolute; left: 70px; top: 284px; list-style: none; }
  .contact {
    display: flex; align-items: center; gap: 10px; height: 28px;
    font-family: "Open Sans", sans-serif; font-size: 17px; color: var(--ink);
  }
  .contact svg { width: 18px; height: 18px; flex: none; }
  .contact-square { width: 18px; height: 18px; border-radius: 4px; background: var(--accent-pink); flex: none; }
</style>
</head>
<body>
<main class="canvas">

  <section class="card card--back" aria-label="Retro del biglietto">
    <div class="brand">
      <span class="brand-dot"></span>
      <span class="brand-name">Velusport Chef</span>
    </div>
  </section>

  <section class="card card--front" aria-label="Fronte del biglietto">
    <svg class="photo" viewBox="0 0 700 400" aria-hidden="false">
      <defs>
        <linearGradient id="photoTone" x1="0" y1="0" x2="1" y2="1">
          <stop offset="0" stop-color="#efe3cf"/>
          <stop offset=".55" stop-color="#d9b25a"/>
          <stop offset="1" stop-color="#8a6a48"/>
        </linearGradient>
      </defs>
      <path d="M410 0 C350 130 370 300 520 400 L700 400 L700 0 Z" fill="var(--peach)"/>
      <path role="img" aria-label="Foto: bambina che mangia spaghetti a tavola con una torta" d="M424 0 C366 130 388 300 540 400 L700 400 L700 0 Z" fill="url(#photoTone)"/>
    </svg>

    <div class="brand">
      <span class="brand-dot"></span>
      <span class="brand-name">Velusport Chef</span>
    </div>

    <div class="person">
      <p class="person-name">Marco Ferretti</p>
      <p class="person-role">Managing Director</p>
    </div>

    <ul class="contacts">
      <li class="contact">
        <svg viewBox="0 0 24 24" aria-hidden="true"><path fill="var(--ink)" d="M6.6 10.8a15.1 15.1 0 0 0 6.6 6.6l2.2-2.2c.3-.3.7-.4 1-.2 1.1.4 2.3.6 3.6.6.6 0 1 .4 1 1V20c0 .6-.4 1-1 1C10.6 21 3 13.4 3 4c0-.6.4-1 1-1h3.5c.6 0 1 .4 1 1 0 1.3.2 2.5.6 3.6.1.3 0 .7-.2 1z"/></svg>
        <span>045-318 726 904</span>
      </li>
      <li class="contact">
        <svg viewBox="0 0 24 24" aria-hidden="true" fill="none" stroke="var(--ink)" stroke-width="1.6"><circle cx="12" cy="12" r="9"/><ellipse cx="12" cy="12" rx="4" ry="9"/><path d="M3 12h18M5 7h14M5 17h14"/></svg>
        <span>www.piattileggerinuovi.it</span>
      </li>
      <li class="contact">
        <span class="contact-square"></span>
        <span>@velusport72</span>
      </li>
    </ul>
  </section>

</main>
</body>
</html>
```